Business card and stationary for eco-aware technology company
Verdalux: Green-minded Scrap Recovery
Business card and stationary for eco-aware technology company - Chemicals
Creative Brief
Professional
Tam Brendow
Managing Director
7-3, 2nd Floor, Pelham Court, Quarry Road, 10450 Georgetown, Penang, Malaysia
+604-8XXXXXX
+6011-5274 XXXX
xxx@verdalux.example
http://www.verdalux.example
YYYYYYY-K
Hello, My name is Tam Brendow, and I am MD of Verdalux. I would like a letterhead and a business card for myself. Verdalux is a Malaysia-based startup with a focus on developing technology for urban mining ( http://scrapharvest.example/ ). Verdalux's name is legally Verdalux Sdn. Bhd., but maybe the shorter form, 'Verdalux' looks better on a business card. Perhaps the "Sdn. Bhd." could be hidden in there somewhere. Up to you! For the business card, the following info should be used: Tam Brendow Managing Director MChem, Ph.D (Chemistry) The back side of the business card can be blank, or it can be very simply decorated. I am on Malaysian time (GMT +8) so please forgive me if my feedback appears delayed. Thanks & good luck, - Tam
Empty is fine. Very simple decoration if you want - maybe just the company logo in the center.
tbrendow tbrendow
Hey, Sorry for the slow feedback. I've just got back to the office. Firstly, I am happy to review the business card designs on this site. However, the stationary designs are too big to preview and quorbasketch's site makes it too slow for me to look at the designs. So, would you designers be able to host the images on a web server, or put them in a .zip file? Private message me the URL and I'll download them and use an image viewer to see them offline. Sorry for the extra work - blame QS's crap design. Ok, now for some feedback: 1) The dark 'Eco' green does not look nice on the card. Please use only a little bit! 2) Lighter greens are nice. Like the colour of the 3 leaves. 3) No transparent cards, please. 4) The back of the card should have a very simple design. Maybe just the 3 leaves on a white background, with no text? 5) I love the designs with the big leaf (#191). It's clever. I also love the designs with the circuit pattern (#212, #213, #214). That's clever too. Private message me if you want more feedback or ideas. I'll try to reply fast. Thanks, - Tam

```html
<!DOCTYPE html>
<html lang="en">
<head>
<meta charset="utf-8">
<title>Verdalux Business Card</title>
<link href="https://fonts.googleapis.com/css2?family=Source+Sans+3:wght@400;600;700&display=swap" rel="stylesheet">
<style>
  :root {
    --page-bg: #ecebe7;
    --card-white: #ffffff;
    --forest: #1f5a2e;
    --leaf: #8dc63f;
    --leaf-deep: #5aa332;
    --brand-green: #3b8a36;
    --ink-light: #ffffff;
    --ink-soft: #d7e7d2;
    --grey: #6f6f6f;
  }
  * { margin: 0; padding: 0; box-sizing: border-box; }
  html, body { width: 1200px; height: 949px; overflow: hidden; }
  body {
    background: var(--page-bg);
    font-family: "Source Sans 3", sans-serif;
    position: relative;
  }
  .business-card {
    position: absolute;
    left: 285px;
    top: 294px;
    width: 630px;
    height: 360px;
    background: var(--card-white);
    box-shadow: 0 6px 18px rgba(0,0,0,0.18);
    overflow: hidden;
  }
  .card-art { position: absolute; inset: 0; }
  .contact-block {
    position: absolute;
    left: 26px;
    top: 40px;
    color: var(--ink-light);
    font-size: 14px;
    line-height: 19px;
  }
  .person-name { font-size: 23px; font-weight: 600; line-height: 28px; }
  .credentials { font-weight: 700; font-size: 13.5px; color: var(--ink-soft); }
  .role { color: var(--ink-soft); margin-top: 2px; }
  .company-details { margin-top: 18px; color: var(--ink-soft); }
  .contact-list { list-style: none; margin-top: 12px; }
  .contact-list li { display: flex; align-items: center; gap: 9px; height: 19.5px; }
  .contact-list svg { width: 12px; height: 12px; flex: none; }
  .brand-mark {
    position: absolute;
    left: 380px;
    top: 158px;
    display: flex;
    flex-direction: column;
  }
  .brand-row { display: flex; align-items: center; gap: 10px; }
  .brand-dot { width: 30px; height: 30px; border-radius: 50%; background: var(--leaf-deep); }
  .brand-name { font-size: 38px; font-weight: 600; color: var(--brand-green); line-height: 40px; }
  .brand-tagline {
    margin-top: 2px;
    margin-left: 40px;
    font-size: 8.5px;
    font-weight: 700;
    letter-spacing: 0.9px;
    color: var(--grey);
  }
</style>
</head>
<body>
  <div class="business-card">
    <svg class="card-art" viewBox="0 0 630 360" width="630" height="360">
      <defs>
        <linearGradient id="stripeGrad" x1="0" y1="0" x2="0" y2="1">
          <stop offset="0" stop-color="#6fb43a"/>
          <stop offset="1" stop-color="#b5dc52"/>
        </linearGradient>
      </defs>
      <polygon points="0,0 272,0 338,360 0,360" fill="var(--forest)"/>
      <polygon points="272,0 292,0 358,360 338,360" fill="url(#stripeGrad)"/>
      <polygon role="img" aria-label="circuit branch motif" points="250,0 340,0 360,190 290,200" fill="var(--leaf)" opacity="0.18"/>
    </svg>

    <div class="contact-block">
      <div class="person-name">Tam Brendow</div>
      <div class="credentials">MChem, Ph.D (Chemistry)</div>
      <div class="role">Managing Director</div>
      <div class="company-details">
        License No YYYYYYY-K<br>
        7-3, 2nd Floor, Pelham Court<br>
        Quarry Road, 10450 Georgetown<br>
        Penang, Malaysia
      </div>
      <ul class="contact-list">
        <li><svg viewBox="0 0 12 12"><path d="M1 4 Q6 0 11 4 L9 5 L8 4 L4 4 L3 5 Z M3 6 H9 L10 11 H2 Z" fill="#fff"/></svg>604-8XXXXXX</li>
        <li><svg viewBox="0 0 12 12"><rect x="3" y="0.5" width="6" height="11" rx="1" fill="#fff"/><rect x="4" y="2" width="4" height="6" fill="var(--forest)"/></svg>6011-5274 XXXX</li>
        <li><svg viewBox="0 0 12 12"><rect x="3" y="0.5" width="6" height="4" fill="#fff"/><rect x="1" y="4.5" width="10" height="5" rx="1" fill="#fff"/><rect x="3" y="8" width="6" height="3.5" fill="#fff"/></svg>604-8XXXXXY</li>
        <li><svg viewBox="0 0 12 12"><rect x="0.5" y="2.5" width="11" height="7" fill="#fff"/><path d="M0.5 2.5 L6 7 L11.5 2.5" stroke="var(--forest)" fill="none"/></svg>info@verdalux.example</li>
        <li><svg viewBox="0 0 12 12"><circle cx="6" cy="6" r="5" fill="none" stroke="#fff" stroke-width="1.2"/><ellipse cx="6" cy="6" rx="2" ry="5" fill="none" stroke="#fff"/><path d="M1 6 H11" stroke="#fff"/></svg>www.verdalux.example</li>
      </ul>
    </div>

    <div class="brand-mark">
      <div class="brand-row">
        <span class="brand-dot"></span>
        <span class="brand-name">Verdalux</span>
      </div>
      <div class="brand-tagline">GREEN-MINDED SCRAP RECOVERY</div>
    </div>
  </div>
</body>
</html>
```